New College Graduate Resume - Creative and unique design that stands out from the rest

Need creative resume design for recent college graduate who graduated from School of Music with a concentration in music composition and production. Striving for a contemporary layout/design that allows the resume to "be unique" and "stand out" but be polished and professional. Open to integrating moderate color/graphics as part of resume design but the design can be minus those attributes as well. Attached is raw content in 7 sections (name/contact info, education, highlights of qualifications, work experience, honors/awards, and professional affiliations). While the designer has full latitude over overall design which (section headers, font type, separation/spacing, use of bullets, justification of text, etc.) please maintain current order/sequence of the 7 sections.

Industry/Entity Type

School

Requirements
Must have
• Name (Tobias Garrick Elwin III) should be most prominent (bold/font size) compared to remainder of resume copy.
• Section headers should be prominent but less so when compared to name on resume.
• The attached file of resume content is provided as raw source copy and is NOT to be just copied and pasted into open fields as is. Expectation is each section of copy will be organized in a manner that is most visually appealing and may include bullets, appropriate spacing, etc.
Should not have
• The attached file of resume content is provided as source copy and is NOT to be just copied and pasted into open fields as is. Expectation is each section of copy will be organized in a manner that

```html
<!DOCTYPE html>
<html lang="en">
<head>
<meta charset="utf-8">
<title>Tobias Garrick Elwin III – Resume</title>
<link href="https://fonts.googleapis.com/css2?family=Arimo:wght@400;700&family=Archivo+Black&display=swap" rel="stylesheet">
<style>
  :root {
    --ink: #2b2b2b;
    --body: #555555;
    --sidebar: #d9d9d9;
    --paper: #ffffff;
    --header-dark: #1c1c1c;
    --header-mid: #6a6a6a;
    --header-light: #bdbdbd;
    --rule: #9a9a9a;
  }
  * { margin: 0; padding: 0; box-sizing: border-box; }
  html, body { width: 1000px; height: 1200px; overflow: hidden; background: var(--paper); }
  body { font-family: "Arimo", Arial, sans-serif; color: var(--body); }

  .resume { position: relative; width: 1000px; height: 1200px; background: var(--paper); }

  .banner {
    position: absolute; left: 0; top: 0; width: 1000px; height: 196px;
    background:
      radial-gradient(ellipse at 78% 70%, rgba(220,220,220,.55), transparent 55%),
      linear-gradient(100deg, var(--header-dark) 0%, var(--header-mid) 35%, var(--header-light) 60%, var(--header-mid) 80%, var(--header-dark) 100%);
  }
  .name-plate {
    position: absolute; left: 145px; top: 55px; width: 708px; height: 62px;
    background: rgba(255,255,255,.88);
    display: flex; align-items: center; justify-content: center;
  }
  .name {
    font-family: "Arimo", Arial, sans-serif; font-weight: 400;
    font-size: 33px; letter-spacing: .5px; color: var(--ink); text-transform: uppercase;
  }
  .contact-strip {
    position: absolute; left: 160px; top: 132px; width: 680px; height: 22px;
    background: rgba(255,255,255,.9);
    font-size: 13.5px; font-weight: 700; color: #4a4a4a;
    display: flex; align-items: center; justify-content: center;
  }

  .sidebar {
    position: absolute; left: 0; top: 196px; width: 347px; height: 1004px;
    background: var(--sidebar); padding: 34px 20px 0 46px;
    font-size: 14.5px; line-height: 17.4px; color: var(--ink);
  }
  .side-heading {
    font-family: "Archivo Black", "Arial Black", sans-serif;
    font-size: 20px; line-height: 21px; color: var(--ink); letter-spacing: .3px;
    margin-bottom: 2px;
  }
  .side-section { margin-bottom: 25px; }

  .main {
    position: absolute; left: 347px; top: 196px; width: 653px; height: 1004px;
    padding: 27px 40px 0 28px;
    font-size: 14.2px; line-height: 17.4px;
  }
  .main-heading {
    font-family: "Arimo", Arial, sans-serif; font-weight: 700;
    font-size: 26px; line-height: 26px; color: var(--ink); letter-spacing: .2px;
  }
  .job { margin-bottom: 23px; }
  .job-meta { font-weight: 700; font-size: 13.8px; color: #4a4a4a; }
  .job-title { font-weight: 700; font-size: 17px; line-height: 20px; color: #3c3c3c; letter-spacing: .3px; }
  .job p { color: var(--body); }

  .divider {
    height: 2px; margin: 0 20px 24px 0;
    background: linear-gradient(90deg, transparent 0%, var(--rule) 50%, transparent 100%);
  }
  .sub-heading { font-weight: 700; font-size: 15.5px; color: var(--ink); letter-spacing: .2px; }
  .list p { color: #333; }
  .list { margin-bottom: 30px; }
</style>
</head>
<body>
<div class="resume">

  <header class="banner" role="img" aria-label="Black and white photograph of hands working a studio mixing console">
    <div class="name-plate"><h1 class="name">Tobias Garrick Elwin III</h1></div>
    <div class="contact-strip">404-555-0182 (cell) | tgelwin552@mailbox.com | 218 Linwood Court Atlanta, Georgia&nbsp;&nbsp;30309</div>
  </header>

  <aside class="sidebar">
    <section class="side-section">
      <h2 class="side-heading">PROFILE</h2>
      <p>Recent graduate of a highly ranked university seeking opportunities to apply composition and production talents across a variety of music genres and other media.</p>
      <p>Expertise lies in delivering high quality sound design, editing, mixing, and recording. Excellent interpersonal skills and the ability to build strong relationships with people at all levels.&nbsp; Exceptionally motivated self-starter and creative problem solver who enjoys working collaboratively on teams.</p>
    </section>
    <section class="side-section">
      <h2 class="side-heading">EDUCATION</h2>
      <p>Bayview University – Harlan School of Music</p>
      <p>Coral Springs, Florida</p>
      <p>Bachelor of Music – May 2016</p>
      <p>Major: Media Writing and Production, GPA 3.20/4.0</p>
      <p>Oakridge Preparatory Academy</p>
      <p>College Park, Georgia</p>
      <p>High School Diploma with Honors – May 2011</p>
    </section>
    <section class="side-section">
      <h2 class="side-heading">HIGHLIGHTS OF QUALIFICATIONS</h2>
      <p>Media Production Software (SoundDesk 11)</p>
      <p>Sound Design</p>
      <p>Sound Acoustics</p>
      <p>Studio Recording</p>
      <p>Audio Editing</p>
      <p>Audio Mixing</p>
      <p>Analog/Digital board operation</p>
      <p>Music Arranging</p>
      <p>Music Composition</p>
      <p>Music Production</p>
      <p>Composing Sheet Music</p>
      <p>Singer-songwriter</p>
      <p>Rhythm guitarist</p>
    </section>
  </aside>

  <main class="main">
    <h2 class="main-heading">WORK EXPERIENCE</h2>

    <article class="job">
      <div class="job-meta">Coastline Picture Works (CPW)<br>Miami, FL<br>May 2014 – Present</div>
      <h3 class="job-title">Sound Engineer</h3>
      <p>Edited and mixed recorded field audio to professional standards.</p>
      <p>Matched audio with motion picture video to create a seamless product.</p>
      <p>Recorded automated dialogue replacement (ADR) audio and integrated into motion picture video project using SoundDesk 11.</p>
      <p>Recorded foley sound effects to be added to film, video, and other media in post-production.</p>
      <p>Composed and recorded original music to accompany various video projects.</p>
    </article>

    <article class="job">
      <div class="job-meta">Brightway Retail Group<br>Atlanta, GA<br>May 2013 - October 2013</div>
      <h3 class="job-title">Sales Associate</h3>
      <p>Provided customer service, maintained a clean and organized work environment, assisted in sales, and performed cashier responsibilities.</p>
    </article>

    <article class="job">
      <div class="job-meta">Peachtree Civic Action League (PCAL)<br>Atlanta, GA<br>June 2012 - August 2012</div>
      <h3 class="job-title">On-Site Promoter/Intern</h3>
      <p>Promoted and advertised various campaigns and managed various office tasks, such as setting up site maps and organizing and sorting non-profit donations.</p>
    </article>

    <article class="job">
      <div class="job-meta">Meridian Direct Sales, Incorporated<br>Atlanta, GA<br>June 2011 – August 2011</div>
      <h3 class="job-title">Product Marketing Consultant</h3>
      <p>Conducted direct sales and marketing of subsidiary product line through establishing a compelling value proposition, overcoming objections, and closing the sale.</p>
    </article>

    <div class="divider"></div>

    <section class="list">
      <h2 class="sub-heading">HONORS/AWARDS</h2>
      <p>Best Film and Score: Frights and Sounds 2015 Competition (Bayview University)</p>
      <p>Leonard B Ashford Scholar</p>
      <p>Best New Member, Delta Kappa Rho Fraternity, Inc.</p>
      <p>Bayview University Homecoming King, 2012</p>
    </section>

    <div class="divider"></div>

    <section class="list">
      <h2 class="sub-heading">PROFESSIONAL AFFILIATION</h2>
      <p>Member, Guild of Contemporary Composers (GCC)</p>
      <p>Member, American Alliance of Songwriters, Composers and Publishers (AASCP)</p>
      <p>Member, Sound Engineering Collective (SEC)</p>
      <p>Member, Delta Kappa Rho Fraternity, Incorporated</p>
    </section>

    <div class="divider"></div>
  </main>

</div>
</body>
</html>
```